Boutique and Spa website design

We need a website for a new business named "Velvet Orchid Boutique and Spa" Base in the state of New York. We sell clothes and accessories as well as spa services:. Microdermabrasion,Peels,Facials,Waxing,Body treatments,.Nails: manicures and pedicures, and massage. We do not sell clothes and accessories on line. I am looking for a spa website.I want this website ready to go. I would like it in HTML/CSS. format.

Target Market(s)

ages 25 to 60

Industry/Entity Type

Business

Font styles to use
Decorative
Script

Colors

Designer to choose colors to be used in the design.

Requirements
Must have
• I want my spa services, my hours, pictures of women getting services (not the pictures below) ,and my logo listed on the website. My hours are Monday and Sunday-Closed and Tues-Friday 10-8....We offer Facials,Microdermabration,Peels,Waxing,eyebrow and eyelash tint, Eyelash extensions, manicure and pedicure, Gel nail polish and shellac,and Massage....Also sell retail skincare products, and women's name brand cloths and accessories...
Nice to have
• Maybe relaxing color tones- browns/purples/greens ....No carton pictures
Should not have
• Prices

```html
<!DOCTYPE html>
<html lang="en">
<head>
<meta charset="utf-8">
<title>Velvet Orchid Boutique and Spa</title>
<link rel="stylesheet" href="https://fonts.googleapis.com/css2?family=PT+Sans:ital,wght@0,400;0,700;1,400&family=Arimo:wght@400;700&display=swap">
<style>
:root{
  --purple:#8f55c9;
  --purple-soft:#ae8dcf;
  --purple-line:#a47bd1;
  --ink:#333;
  --body:#555;
  --muted:#999;
  --hero-bg:#efefef;
  --footer:#1f1f1f;
  --black:#0b0b0b;
  --white:#fff;
}
*{margin:0;padding:0;box-sizing:border-box}
html,body{width:1200px;height:1077px;overflow:hidden}
body{position:relative;background:var(--white);font-family:"PT Sans",sans-serif;color:var(--ink)}
.abs{position:absolute}
a{color:inherit;text-decoration:none}

/* header */
.site-header{left:0;top:0;width:1200px;height:86px;background:#fcfbfc;border-bottom:1px solid var(--purple-line)}
.brand{left:237px;top:22px;display:flex;align-items:center;gap:10px;color:var(--purple);font-size:22px;line-height:1.05}
.brand-dot{width:34px;height:34px;border-radius:50%;background:var(--purple)}
.brand small{display:block;font-size:22px}
.nav{left:0;top:0;height:86px;width:1200px}
.nav a{position:absolute;top:58px;font-size:8.5px;color:#444;text-transform:uppercase;transform:translateX(-50%);white-space:nowrap}
.nav a.active{color:var(--purple);font-weight:700}
.nav-bar{left:684px;top:82px;width:41px;height:4px;background:var(--purple)}

/* hero */
.hero{left:0;top:86px;width:1200px;height:316px;background:var(--hero-bg);border-bottom:1px solid var(--purple-line)}
.hero-photo{left:614px;top:86px;width:368px;height:316px;background:linear-gradient(90deg,#e8e8e8,#cfcfcf 55%,#e6e6e6)}
.hero-title{left:236px;top:212px;width:270px;height:76px;background:linear-gradient(90deg,#fff 55%,rgba(255,255,255,0))}
.hero-title::before{content:"";position:absolute;left:0;top:0;width:100%;height:5px;background:linear-gradient(90deg,var(--purple),rgba(143,85,201,0))}
.hero-title h1{position:absolute;left:15px;top:26px;font-weight:400;font-size:27px;color:var(--purple);letter-spacing:.3px}
.video-btn{left:236px;top:328px;width:121px;height:23px;background:var(--purple);color:#fff;font-size:8.5px;line-height:23px;padding-left:9px}
.video-btn svg{position:absolute;left:72px;top:-8px}
.slide-arrow{top:351px;width:28px;height:24px;background:#8a8a8a}
.slide-arrow svg{display:block;margin:5px auto 0}

/* content */
.content-bg{left:0;top:403px;width:1200px;height:521px;background:linear-gradient(#f4efee,#fff 45%)}
.ph-spa{left:236px;top:452px;width:368px;height:128px;background:linear-gradient(90deg,#e7e3e4,#cfd3d8 40%,#e8e6e3 75%,#c8ccd2)}
.ph-stone{left:613px;top:452px;width:180px;height:128px;background:linear-gradient(135deg,#efe6dc,#c99d80)}
.ph-facial{left:801px;top:452px;width:181px;height:128px;background:linear-gradient(135deg,#f6f1ee,#e5c3b0)}
.side-col{left:801px;top:580px;width:181px;height:333px;background:var(--purple-soft)}

.heading{font-size:13px;font-weight:400;color:#444}
.heading b{color:var(--purple);font-weight:700}
.heading.on-purple,.heading.on-purple b{color:#fff}
.rule{height:1px;background:#ddd}
.rule::before{content:"";position:absolute;left:0;top:-1px;width:38px;height:2px;background:var(--purple)}
.text{font-family:Arimo,sans-serif;font-size:7.3px;line-height:13px;color:var(--body)}
.text.dark{color:#222}
.text.light{color:#fff}
.more{font-family:Arimo,sans-serif;font-size:6.3px;font-weight:700;color:#555;text-decoration:underline;text-transform:uppercase}
.more.light{color:#fff}
.sub{font-size:8px;color:var(--muted)}
.sub.light{color:#f1e9f8}
.side-rule{height:1px;background:rgba(255,255,255,.55)}
.side-rule::before{content:"";position:absolute;left:0;top:-1px;width:38px;height:2px;background:#8b63b5}

.view-all{left:537px;top:736px;width:67px;height:20px;background:var(--purple);color:#fff;font-size:8px;font-weight:700;text-align:center;line-height:20px}
.news-head{font-size:8px;font-weight:700;color:var(--purple)}
.date{font-size:6.5px;color:var(--muted)}
.mini-arrow{width:11px;height:10px;background:#a5a5a5}
.mini-arrow.on{background:var(--purple)}
.mini-arrow.pale{background:#cdb8e2}
.mini-arrow svg{display:block;margin:2px auto 0}
.thumb{width:83px;height:62px}
.thumb svg{position:absolute;left:32px;top:22px}
.quote-box{left:801px;top:776px;width:181px;height:82px;background:var(--black);color:#fff}
.quote-box::after{content:"";position:absolute;left:84px;bottom:-6px;border:6px solid transparent;border-bottom:0;border-top-color:var(--black)}
.quote-mark{left:12px;top:8px;font-family:Georgia,serif;font-size:20px;font-weight:700}
.quote-box p{left:12px;top:24px;width:160px}
.author{left:801px;top:870px;width:181px;text-align:center;color:#fff;font-size:8.5px}
.author em{display:block;font-size:7px;margin-top:1px}

/* footer */
.site-footer{left:0;top:924px;width:1200px;height:153px;background:var(--footer)}
.foot-brand{left:0;top:958px;width:1200px;text-align:center;color:#d8d8d8;font-size:24px;line-height:1.1}
.foot-brand span{display:inline-block;width:30px;height:30px;border-radius:50%;background:#d8d8d8;vertical-align:-4px;margin-right:10px}
.foot-line{left:468px;top:1037px;width:217px;height:1px;background:#555}
.foot-links{left:0;top:1047px;width:1200px;text-align:center;font-family:Arimo,sans-serif;font-size:6.8px;color:#bbb;line-height:10px}
</style>
</head>
<body>

<header class="site-header abs"></header>
<div class="brand abs"><span class="brand-dot"></span><div>Velvet Orchid<small>Boutique and Spa</small></div></div>
<nav class="nav abs">
  <a class="active" href="#" style="left:703px">Home</a>
  <a href="#" style="left:772px">Our Services</a>
  <a href="#" style="left:842px">Gallery</a>
  <a href="#" style="left:900px">Blogs</a>
  <a href="#" style="left:961px">Contact Us</a>
</nav>
<div class="nav-bar abs"></div>

<section class="hero abs"></section>
<div class="hero-photo abs" role="img" aria-label="Black and white portrait of a woman in profile touching her neck"></div>
<div class="hero-title abs"><h1>FLAWLESS BEAUTY</h1></div>
<a class="video-btn abs" href="#">Watch &nbsp;Our Video
  <svg width="38" height="38" viewBox="0 0 38 38"><circle cx="19" cy="19" r="17.5" fill="#fff" stroke="#8f55c9" stroke-width="2"/><path d="M16 13l9 6-9 6z" fill="#111"/></svg>
</a>
<div class="slide-arrow abs" style="left:920px"><svg width="10" height="14"><path d="M8 1L2 7l6 6" fill="none" stroke="#fff" stroke-width="1.6"/></svg></div>
<div class="slide-arrow abs" style="left:953px"><svg width="10" height="14"><path d="M2 1l6 6-6 6" fill="none" stroke="#fff" stroke-width="1.6"/></svg></div>

<div class="content-bg abs"></div>
<div class="ph-spa abs" role="img" aria-label="White orchids, rolled towel and spa stones"></div>
<div class="ph-stone abs" role="img" aria-label="Woman receiving a hot stone massage"></div>
<div class="ph-facial abs" role="img" aria-label="Woman receiving a relaxing facial"></div>
<div class="side-col abs"></div>

<!-- welcome -->
<h2 class="heading abs" style="left:236px;top:591px">Welcome <b>to Velvet Orchid</b></h2>
<div class="rule abs" style="left:236px;top:612px;width:368px"></div>
<p class="text abs" style="left:236px;top:623px;width:368px">Velvet Orchid Boutique and Spa is a calm retreat in New York where you can unwind, refresh your skin and leave feeling your best. Our licensed team offers facials, peels, waxing, lash and brow care, nails and massage, each tailored to you in a quiet and welcoming space.</p>
<p class="text dark abs" style="left:236px;top:670px;width:368px">Visit our boutique for retail skincare products and women's name brand clothes and accessories, available in store only.</p>

<h2 class="heading abs" style="left:613px;top:591px">Our <b>Services</b></h2>
<div class="rule abs" style="left:613px;top:612px;width:180px"></div>
<p class="text abs" style="left:613px;top:623px;width:180px">Facials, microdermabrasion, peels, waxing, brow and lash tint, lash extensions, manicure, pedicure, gel, shellac and massage.</p>
<a class="more abs" href="#" style="left:613px;top:675px">Read More</a>

<h2 class="heading on-purple abs" style="left:814px;top:591px">Opening <b>Hours</b></h2>
<div class="side-rule abs" style="left:814px;top:612px;width:154px"></div>
<p class="text light abs" style="left:814px;top:623px;width:156px">Tuesday to Friday: 10am to 8pm<br>Monday and Sunday: Closed<br>Walk-ins welcome, booking advised.</p>
<a class="more light abs" href="#" style="left:814px;top:675px">Read More</a>

<!-- news -->
<h2 class="heading abs" style="left:236px;top:731px">Latest <b>News</b></h2>
<p class="sub abs" style="left:236px;top:748px">Spa and boutique updates</p>
<a class="view-all abs" href="#">view all &gt;&gt;</a>
<div class="rule abs" style="left:236px;top:765px;width:368px"></div>
<h3 class="news-head abs" style="left:236px;top:776px">Eyelash extensions now offered</h3>
<p class="date abs" style="left:236px;top:793px">February 17,2014</p>
<p class="text abs" style="left:236px;top:808px;width:170px">Full or natural sets applied by our lash artist, plus brow and lash tint to frame your eyes for weeks of easy beauty [....]</p>
<a class="more abs" href="#" style="left:236px;top:861px">Read More</a>
<h3 class="news-head abs" style="left:424px;top:776px">New season in the boutique</h3>
<p class="date abs" style="left:424px;top:793px">February 17,2014</p>
<p class="text abs" style="left:424px;top:808px;width:170px">Fresh name brand clothes and accessories have arrived in store, alongside our new range of retail skincare [....]</p>
<a class="more abs" href="#" style="left:424px;top:861px">Read More</a>

<!-- gallery -->
<h2 class="heading abs" style="left:613px;top:731px">From <b>Gallery</b></h2>
<p class="sub abs" style="left:613px;top:748px">Moments at our spa</p>
<div class="mini-arrow abs" style="left:767px;top:735px"><svg width="6" height="6"><path d="M5 0L1 3l4 3" fill="none" stroke="#fff"/></svg></div>
<div class="mini-arrow on abs" style="left:782px;top:735px"><svg width="6" height="6"><path d="M1 0l4 3-4 3" fill="none" stroke="#fff"/></svg></div>
<div class="rule abs" style="left:613px;top:765px;width:180px"></div>
<div class="thumb abs" style="left:613px;top:779px;background:linear-gradient(135deg,#6e5a4d,#c9b2a1)" role="img" aria-label="Woman with styled hair"></div>
<div class="thumb abs" style="left:710px;top:779px;background:linear-gradient(135deg,#f3efec,#e2b9a6)" role="img" aria-label="Facial treatment"><svg width="18" height="18"><circle cx="9" cy="9" r="9" fill="rgba(255,255,255,.35)"/><path d="M9 5v8M5 9h8" stroke="#fff"/></svg></div>
<div class="thumb abs" style="left:613px;top:851px;background:linear-gradient(135deg,#d8b7a0,#8a6a58)" role="img" aria-label="Hot stone massage"><svg width="18" height="18"><circle cx="9" cy="9" r="9" fill="rgba(255,255,255,.35)"/><path d="M9 5v8M5 9h8" stroke="#fff"/></svg></div>
<div class="thumb abs" style="left:710px;top:851px;background:linear-gradient(135deg,#f1d9d6,#d89aa3)" role="img" aria-label="Pedicure with flower petals"><svg width="18" height="18"><circle cx="9" cy="9" r="9" fill="rgba(255,255,255,.35)"/><path d="M9 5v8M5 9h8" stroke="#fff"/></svg></div>

<!-- testimonial -->
<h2 class="heading on-purple abs" style="left:813px;top:731px;font-weight:700">Testimonial</h2>
<p class="sub light abs" style="left:813px;top:748px">What our clients say</p>
<div class="mini-arrow pale abs" style="left:944px;top:735px"><svg width="6" height="6"><path d="M5 0L1 3l4 3" fill="none" stroke="#fff"/></svg></div>
<div class="mini-arrow pale abs" style="left:960px;top:735px"><svg width="6" height="6"><path d="M1 0l4 3-4 3" fill="none" stroke="#fff"/></svg></div>
<div class="side-rule abs" style="left:813px;top:765px;width:156px"></div>
<div class="quote-box abs">
  <span class="quote-mark abs">&ldquo;</span>
  <p class="text light abs">The facial was the most relaxing hour of my month. My skin glowed for days and the staff made me feel truly pampered.</p>
</div>
<p class="author abs">By Laura M.<em>Spa Client</em></p>

<!-- footer -->
<footer class="site-footer abs"></footer>
<div class="foot-brand abs"><span></span>Velvet Orchid Boutique and Spa</div>
<div class="foot-line abs"></div>
<div class="foot-links abs">
  <p>Home | Our Service | Gallery | Blog | Contact Us</p>
  <p>Copyright 2014. All Right Reserved.</p>
</div>

</body>
</html>
```